Dwellcraft Brochure

We need a brochure on A4 to show our portfolio and invite people to take up our service offering. This brochure will be mailed to peoples home in the areas that we are targeting. We offer quick house modifications including bathroom and kitchen renovations, disability access, security, extensions and full house renovations as well as design and build services.

Target Market(s)

Home Owners, Occupational Therapists, Retirement village, Medical Centers

Industry/Entity Type

Construction and Design

Requirements
Must have
• Photos and our services listed and an invitation to use them

```html
<!DOCTYPE html>
<html lang="en">
<head>
<meta charset="UTF-8">
<title>Dwellcraft Brochure</title>
<link href="https://fonts.googleapis.com/css2?family=Alex+Brush&family=Bebas+Neue&family=Raleway:wght@300;400;600&display=swap" rel="stylesheet">
<style>
  :root {
    --brand-red: #c8202f;
    --ink-grey: #5a5a5c;
    --soft-grey: #8a8a8d;
    --page: #ffffff;
    --backdrop: #ffffff;
    --shadow-text: #d9d9d9;
  }
  * { margin: 0; padding: 0; box-sizing: border-box; }
  html, body {
    width: 960px; height: 1200px; overflow: hidden;
    background: var(--backdrop);
  }
  .brochure {
    position: relative; width: 960px; height: 1200px;
    background: var(--page);
    font-family: "Raleway", sans-serif;
  }
  .site-url {
    position: absolute; top: 38px; left: 0; width: 100%;
    text-align: center; font-weight: 300; font-size: 24px;
    color: var(--soft-grey); letter-spacing: 0.5px;
  }
  .headline {
    position: absolute; top: 68px; left: 0; width: 100%;
    text-align: center;
    font-family: "Alex Brush", cursive; font-weight: 400;
    font-size: 140px; line-height: 1; color: var(--brand-red);
    text-shadow: 4px 4px 0 var(--shadow-text);
  }
  .offer-title {
    position: absolute; top: 232px; left: 0; width: 100%;
    text-align: center; font-family: "Bebas Neue", sans-serif; font-weight: 400;
    font-size: 46px; color: var(--brand-red); line-height: 1;
  }
  .offer-list {
    position: absolute; top: 278px; left: 60px; width: 840px;
    text-align: center; font-family: "Bebas Neue", sans-serif;
    font-size: 28px; line-height: 1.15; color: var(--ink-grey);
  }
  .portfolio { position: absolute; inset: 0; pointer-events: none; }
  .photo { position: absolute; }
  .photo-dining {
    left: 70px; top: 370px; width: 420px; height: 265px;
    background: linear-gradient(180deg, #eef0f1 0%, #dfe1e2 55%, #c48a4a 75%, #3a3a3a 100%);
  }
  .photo-kitchen {
    left: 510px; top: 385px; width: 380px; height: 310px;
    background: linear-gradient(160deg, #c9a273 0%, #e9e6e1 40%, #f3f3f3 65%, #a6a29d 100%);
  }
  .photo-ramp {
    left: 60px; top: 655px; width: 420px; height: 270px;
    background: linear-gradient(180deg, #4d7fc4 0%, #9fb7d2 30%, #d8dadc 55%, #8c5a44 78%, #2d2d2d 100%);
  }
  .photo-bathroom {
    left: 500px; top: 715px; width: 370px; height: 240px;
    background: linear-gradient(135deg, #8f8f8f 0%, #bdbdbd 45%, #f1f1f1 70%, #8b5a36 100%);
  }
  .join-mark {
    position: absolute; left: 455px; top: 615px; width: 70px; height: 70px;
  }
  .contact {
    position: absolute; left: 60px; top: 985px; width: 400px;
    text-align: center; color: var(--ink-grey);
  }
  .contact-invite { font-weight: 300; font-size: 22px; line-height: 1.2; }
  .contact-phone {
    font-family: "Bebas Neue", sans-serif; font-size: 52px;
    color: var(--brand-red); line-height: 1.05; margin-top: 6px;
  }
  .contact-email { font-weight: 300; font-size: 20px; margin-top: 2px; }
  .brand {
    position: absolute; left: 500px; top: 1020px; width: 390px;
    text-align: center;
  }
  .brand-name {
    display: flex; align-items: center; justify-content: center; gap: 12px;
    font-weight: 600; font-size: 44px; letter-spacing: 1px;
    color: var(--brand-red); line-height: 1;
  }
  .brand-square {
    flex: 0 0 20px; width: 20px; height: 20px; background: var(--brand-red);
  }
  .brand-sub {
    display: flex; align-items: center; gap: 12px;
    margin-top: 12px; font-weight: 400; font-size: 21px;
    color: var(--ink-grey); white-space: nowrap;
  }
  .brand-sub::before, .brand-sub::after {
    content: ""; flex: 1; height: 2px; background: var(--ink-grey);
  }
</style>
</head>
<body>
<main class="brochure">
  <p class="site-url">www.dwellcraft.com.au</p>
  <h1 class="headline">Live the dream!</h1>
  <h2 class="offer-title">We offer:</h2>
  <p class="offer-list">Quick house modifications including bathroom and kitchen renovations,<br>disability access, security, extensions and full house renovations.</p>

  <section class="portfolio">
    <div class="photo photo-dining" role="img" aria-label="Photo of a renovated open-plan kitchen and dining room with timber table and black wire chairs"></div>
    <div class="photo photo-kitchen" role="img" aria-label="Photo of a renovated kitchen with timber overhead cabinets, white tiles and a concrete benchtop"></div>
    <div class="photo photo-ramp" role="img" aria-label="Photo of a house exterior with a new disability access ramp and handrails"></div>
    <div class="photo photo-bathroom" role="img" aria-label="Photo of a renovated grey-tiled bathroom with freestanding bath and timber vanity"></div>
    <svg class="join-mark" viewBox="0 0 80 80" aria-hidden="true">
      <rect x="33" y="0" width="14" height="80" fill="#c8202f"/>
      <rect x="0" y="33" width="80" height="14" fill="#c8202f"/>
    </svg>
  </section>

  <section class="contact">
    <p class="contact-invite">Call now<br>for a free quote</p>
    <p class="contact-phone">(03) 9012-4478</p>
    <p class="contact-email">info@dwellcraft.com.au</p>
  </section>

  <section class="brand">
    <p class="brand-name"><span class="brand-square"></span>DWELLCRAFT</p>
    <p class="brand-sub">by Larkfield Builders</p>
  </section>
</main>
</body>
</html>
```